Poster of Insipirational Quotes

Attached is a list of leadership quotes from Harold Brenwick. I would like a poster made, incorporating whatever design elements you like, potentially including Harold's face, and one or more of the quotes. I intend to print this out in A3 or larger to hang on my wall.

The quotes are:

Being responsible sometimes means pissing people off.

The day soldiers stop bringing you their problems is the day you have stopped leading them.

Don't be buffaloed by experts and elites. Experts often possess more data than judgment. Elites can become so inbred that they produce hemophiliacs who bleed to death as soon as they are nicked by the real world.

Don't be afraid to challenge the pros, even in their own backyard.

Never neglect details. When everyone's mind is dulled or distracted the leader must be doubly vigilant.

You don't know what you can get away with until you try.

Keep looking below surface appearances. Don't shrink from doing so (just) because you might not like what you find.

Organization doesn't really accomplish anything. Plans don't accomplish anything, either. Theories of management don't much matter. Endeavors succeed or fail because of the people involved. Only by attracting the best people will you accomplish great deeds.

Organization charts and fancy titles count for next to nothing.

Never let your ego get so close to your position that when your position goes, your ego goes with it.

Fit no stereotypes. Don't chase the latest management fads. The situation dictates which approach best accomplishes the team's mission.

Perpetual optimism is a force multiplier.

Look for intelligence and judgment, and most critically, a capacity to anticipate, to see around corners. Also look for loyalty, integrity, a high energy drive, a balanced ego, and the drive to get things done.

Great leaders are almost always great simplifiers, who can cut through argument, debate and doubt, to offer a solution everybody can understand.

The commander in the field is always right and the rear echelon is wrong, unless proved otherwise.

Have fun in your command. Don't always run at a breakneck pace. Take leave when you've earned it: Spend time with your families. Corollary: surround yourself with people who take their work seriously, but not themselves, those who work hard and play hard.

Command is lonely.

Leadership is the art of accomplishing more than the science of management
says is possible.

I need to modify the specification based on the designs that I've seen.

Executive Office

Designer to choose colors to be used in the design.

• Quotes

```html
<!DOCTYPE html>
<html lang="en">
<head>
<meta charset="utf-8">
<title>Leadership Quotes – Harold Brenwick</title>
<link rel="stylesheet" href="https://fonts.googleapis.com/css2?family=Crimson+Pro:ital,wght@1,400&display=swap">
<style>
  :root {
    --paper: #ffffff;
    --ink: #1c1c1c;
    --panel-top: #fbfaf6;
    --panel-mid: #e8e1cf;
    --panel-low: #f3efe6;
    --portrait-light: #e4dfd2;
    --portrait-mid: #cfc8b6;
    --portrait-dark: #b8b19d;
    --edge-shadow: rgba(90, 84, 50, 0.45);
  }
  * { margin: 0; padding: 0; box-sizing: border-box; }
  html, body {
    width: 1200px;
    height: 900px;
    overflow: hidden;
    background: var(--paper);
  }
  .poster {
    position: relative;
    width: 1200px;
    height: 900px;
    background: var(--paper);
    overflow: hidden;
  }
  .portrait-panel {
    position: absolute;
    left: 0;
    top: 0;
    width: 345px;
    height: 900px;
    background: linear-gradient(to bottom, var(--panel-top) 0%, var(--panel-mid) 45%, var(--panel-mid) 70%, var(--panel-low) 100%);
    box-shadow: 3px 0 6px var(--edge-shadow);
  }
  .portrait {
    position: absolute;
    left: 0;
    top: 110px;
    width: 345px;
    height: 660px;
  }
  .quote-list {
    position: absolute;
    left: 388px;
    top: 56px;
    width: 786px;
    list-style: none;
    font-family: "Crimson Pro", "Georgia", serif;
    font-style: italic;
    font-size: 16px;
    line-height: 18.5px;
    color: var(--ink);
  }
  .quote {
    position: relative;
    margin-bottom: 18.5px;
  }
  .quote::before {
    content: "";
    position: absolute;
    left: -13px;
    top: 8px;
    width: 5px;
    height: 5px;
    border-radius: 50%;
    background: var(--ink);
  }
</style>
</head>
<body>
<main class="poster">
  <aside class="portrait-panel">
    <svg class="portrait" viewBox="0 0 345 660" role="img" aria-label="Stippled portrait of Harold Brenwick in glasses, suit and tie, fading into the panel">
      <defs>
        <radialGradient id="portrait-tone" cx="40%" cy="45%" r="60%">
          <stop offset="0%" stop-color="var(--portrait-light)"/>
          <stop offset="55%" stop-color="var(--portrait-mid)"/>
          <stop offset="100%" stop-color="var(--portrait-dark)" stop-opacity="0"/>
        </radialGradient>
      </defs>
      <rect x="0" y="0" width="345" height="660" fill="url(#portrait-tone)"/>
    </svg>
  </aside>

  <ul class="quote-list">
    <li class="quote">Being responsible sometimes means pissing people off.</li>
    <li class="quote">The day soldiers stop bringing you their problems is the day you have stopped leading them.</li>
    <li class="quote">Don't be buffaloed by experts and elites. Experts often possess more data than judgment. Elites can become so inbred that they produce hemophiliacs who bleed to death as soon as they are nicked by the real world.</li>
    <li class="quote">Don't be afraid to challenge the pros, even in their own backyard.</li>
    <li class="quote">Never neglect details. When everyone's mind is dulled or distracted the leader must be doubly vigilant.</li>
    <li class="quote">You don't know what you can get away with until you try.</li>
    <li class="quote">Keep looking below surface appearances. Don't shrink from doing so (just) because you might not like what you find.</li>
    <li class="quote">Organization doesn't really accomplish anything. Plans don't accomplish anything, either. Theories of management don't much matter. Endeavors succeed or fail because of the people involved. Only by attracting the best people will you accomplish great deeds.</li>
    <li class="quote">Organization charts and fancy titles count for next to nothing.</li>
    <li class="quote">Never let your ego get so close to your position that when your position goes, your ego goes with it.</li>
    <li class="quote">Fit no stereotypes. Don't chase the latest management fads. The situation dictates which approach best accomplishes the team's mission.</li>
    <li class="quote">Perpetual optimism is a force multiplier.</li>
    <li class="quote">Look for intelligence and judgment, and most critically, a capacity to anticipate, to see around corners. Also look for loyalty, integrity, a high energy drive, a balanced ego, and the drive to get things done.</li>
    <li class="quote">Great leaders are almost always great simplifiers, who can cut through argument, debate and doubt, to offer a solution everybody can understand.</li>
    <li class="quote">The commander in the field is always right and the rear echelon is wrong, unless proved otherwise.</li>
    <li class="quote">Have fun in your command. Don't always run at a breakneck pace. Take leave when you've earned it: Spend time with your families. Corollary: surround yourself with people who take their work seriously, but not themselves, those who work hard and play hard.</li>
    <li class="quote">Command is lonely.</li>
    <li class="quote">Leadership is the art of accomplishing more than the science of management<br>says is possible.</li>
  </ul>
</main>
</body>
</html>
```